FACEBOOK PAGE FOR BREVLO PLUMBING GROUP

We need a facebook banner for our new plumbing business.

Needs to be catchy and inline with our logo.

Phone: 0472 836 291
Email: hello@brevlo.com.au
website: www.brevlo.com.au
Servicing: Perth Metro Areas and surrounding suburbs
Services:
*We offer a wide range of services, including:
Plumbing – General maintenance, blocked drains, toilet repairs, burst pipes, reticulation, renovations & emergencies.

*Hot Water – Installation, servicing & repairs for all systems.

*Cooling & Heating – Air conditioning, evaporative cooling & heater servicing.

*Filtration – Filtered taps, under-sink systems & whole-house filtration setups.

Our Mission

Brevlo Group believes plumbing shouldn't break the bank - or your trust. Our mission is to provide honest, affordable, and no-nonsense plumbing services that get the job done right the first time. No runaround - just reliable work, and the respect every customer deserves.

What Makes Us Different???

Upfront Fixed Pricing
No surprises, no hidden fees. You get clear, honest quotes before any work begins.

Respectful, Customer-First Service
We show up on time, communicate clearly, and treat your property like it’s our own.

Locals Serving Locals
We’re proud to support the Perth community with reliable, high-quality plumbing backed by real local care.

FOR THE DESIGNER A little background on us as a new biz for your reference:
By Locals, For Locals
After 13 years in the plumbing industry, seasoned local plumber Wade founded his company to address the widespread issue of homeowners and businesses being overcharged or receiving inferior work. He knew there had to be a better way—and that’s when Brevlo was created.
Today, Brevlo Group is a trusted plumbing company based in Osborne Park, proudly serving residential, commercial, and industrial clients across the Perth metro area. With over a decade of experience, we deliver expert workmanship, fair pricing, and treat every job—big or small—with the same care and professionalism.
Need it done right—and affordably? Get it sorted with BREVLO now!

```html
<!DOCTYPE html>
<html lang="en">
<head>
<meta charset="utf-8">
<title>Brevlo Plumbing Group – Facebook Cover</title>
<link rel="stylesheet" href="https://fonts.googleapis.com/css2?family=Montserrat:wght@500;600;700;800&display=swap">
<style>
  :root {
    --navy: #2b2d6b;
    --brand-blue: #1a64b0;
    --panel-top: #1f4d91;
    --panel-bottom: #0a9fe0;
    --tick-blue: #1ea7e4;
    --tab-text: #1f5aa0;
    --white: #ffffff;
    --bg-light: #eef2f6;
    --bg-mid: #e3e8ee;
  }
  * { margin: 0; padding: 0; box-sizing: border-box; }
  html, body { width: 1200px; height: 440px; overflow: hidden; background: var(--white); }
  .cover {
    position: relative;
    width: 1200px;
    height: 440px;
    overflow: hidden;
    font-family: "Montserrat", sans-serif;
  }
  .backdrop-photo {
    position: absolute; inset: 0;
    background: radial-gradient(ellipse at 45% 50%, var(--bg-light) 0%, var(--bg-mid) 100%);
  }
  .brand-name {
    position: absolute;
    left: 191px; top: 86px;
    font-size: 88px;
    font-weight: 700;
    letter-spacing: 22px;
    line-height: 1;
    color: var(--brand-blue);
  }
  .tagline {
    position: absolute;
    left: 192px; top: 190px;
    color: var(--navy);
    font-weight: 700;
    line-height: 1;
  }
  .tagline .line-one { display: block; font-size: 30px; letter-spacing: 19.2px; }
  .tagline .line-two { display: block; font-size: 30px; letter-spacing: 8.2px; margin-top: 3px; }
  .benefits {
    position: absolute;
    left: 193px; top: 280px;
    list-style: none;
  }
  .benefits li {
    display: flex; align-items: center;
    height: 31px; margin-bottom: 8px;
    color: var(--navy);
    font-size: 27px; font-weight: 600;
  }
  .benefits .tick {
    width: 31px; height: 31px;
    background: var(--tick-blue);
    margin-right: 13px;
    display: flex; align-items: center; justify-content: center;
  }
  .service-panel {
    position: absolute;
    left: 835px; top: 0;
    width: 365px; height: 440px;
    background: linear-gradient(150deg, var(--panel-top) 0%, #1477c4 55%, var(--panel-bottom) 100%);
  }
  .services {
    position: absolute;
    left: 870px; top: 78px;
    list-style: none;
  }
  .services li {
    display: flex; align-items: center;
    height: 44px;
    color: var(--white);
    font-size: 28px; font-weight: 700;
  }
  .services svg { width: 28px; height: 28px; margin-right: 14px; flex: none; }
  .service-area {
    position: absolute;
    left: 835px; top: 309px;
    width: 303px; height: 71px;
    background: #f3f6fa;
    border-radius: 0 14px 14px 0;
    padding: 16px 0 0 12px;
    color: var(--tab-text);
    font-weight: 700;
    line-height: 1;
  }
  .service-area .area-main { display: block; font-size: 20.5px; letter-spacing: 0.3px; }
  .service-area .area-sub { display: block; font-size: 14.8px; letter-spacing: 0.55px; margin-top: 5px; }
  .contact-row {
    position: absolute;
    left: 843px; top: 415px;
    display: flex; align-items: center;
    color: var(--white);
    font-size: 10.5px; font-weight: 500;
  }
  .contact-row span { display: flex; align-items: center; margin-right: 14px; }
  .contact-row span:last-child { margin-right: 0; }
  .contact-row svg { width: 12px; height: 12px; margin-right: 6px; }
</style>
</head>
<body>
<div class="cover">
  <div class="backdrop-photo" role="img" aria-label="Faded photograph of chrome plumbing pipes and fittings"></div>

  <div class="brand-name">BREVLO</div>

  <h1 class="tagline">
    <span class="line-one">RELIABLE LOCAL</span>
    <span class="line-two">PLUMBING SERVICES</span>
  </h1>

  <ul class="benefits">
    <li><span class="tick"><svg width="18" height="14" viewBox="0 0 18 14"><path d="M2 7 L7 12 L16 2" fill="none" stroke="#fff" stroke-width="2.6" stroke-linecap="round" stroke-linejoin="round"/></svg></span>Fixed Pricing No Hidden Fees</li>
    <li><span class="tick"><svg width="18" height="14" viewBox="0 0 18 14"><path d="M2 7 L7 12 L16 2" fill="none" stroke="#fff" stroke-width="2.6" stroke-linecap="round" stroke-linejoin="round"/></svg></span>Local &amp; Trusted</li>
    <li><span class="tick"><svg width="18" height="14" viewBox="0 0 18 14"><path d="M2 7 L7 12 L16 2" fill="none" stroke="#fff" stroke-width="2.6" stroke-linecap="round" stroke-linejoin="round"/></svg></span>Respectful Service</li>
  </ul>

  <div class="service-panel"></div>

  <ul class="services">
    <li>
      <svg viewBox="0 0 28 28" aria-hidden="true"><path d="M3 8h12v-3h4v14h-4v-6H8v3H3z" fill="#fff"/><path d="M5 17c-1.5 2.5-1.5 4 0 4s1.5-1.5 0-4z" fill="#fff"/><path d="M17 16l8 8" stroke="#fff" stroke-width="3" stroke-linecap="round"/></svg>
      Plumbing
    </li>
    <li>
      <svg viewBox="0 0 28 28" aria-hidden="true"><path d="M14 2c2 5 9 8 9 16a9 9 0 0 1-18 0c0-4 2-6 4-8 0 3 1 5 3 5-1-5 0-9 2-13z" fill="#fff"/></svg>
      Hot Water
    </li>
    <li>
      <svg viewBox="0 0 28 28" aria-hidden="true"><g stroke="#fff" stroke-width="2.2" stroke-linecap="round"><path d="M14 2v24M3.6 8l20.8 12M3.6 20l20.8-12"/><path d="M11 4l3 3 3-3M11 24l3-3 3 3"/></g></svg>
      Cooling &amp; Heating
    </li>
    <li>
      <svg viewBox="0 0 28 28" aria-hidden="true"><circle cx="8" cy="3" r="1.6" fill="#fff"/><circle cx="14" cy="3" r="1.6" fill="#fff"/><circle cx="20" cy="3" r="1.6" fill="#fff"/><path d="M2 8h24l-9 9v9h-6v-9z" fill="#fff"/></svg>
      Filtration
    </li>
  </ul>

  <div class="service-area">
    <span class="area-main">SERVICING PERTH METRO</span>
    <span class="area-sub">AREAS &amp; SURROUNDING SUBURBS</span>
  </div>

  <div class="contact-row">
    <span><svg viewBox="0 0 12 12" aria-hidden="true"><path d="M2.5 1l2 2.5-1.2 1.3a6 6 0 0 0 3.9 3.9L8.5 7.5 11 9.5 9.8 11C5 11 1 7 1 2.2z" fill="#fff"/></svg>0472 836 291</span>
    <span><svg viewBox="0 0 12 12" aria-hidden="true"><rect x="0.5" y="2" width="11" height="8" fill="none" stroke="#fff" stroke-width="1.2"/><path d="M0.5 2l5.5 4.5L11.5 2" fill="none" stroke="#fff" stroke-width="1.2"/></svg>hello@brevlo.com.au</span>
    <span><svg viewBox="0 0 12 12" aria-hidden="true"><g fill="none" stroke="#fff" stroke-width="1"><circle cx="6" cy="6" r="5"/><ellipse cx="6" cy="6" rx="2.2" ry="5"/><path d="M1 6h10M2 3.5h8M2 8.5h8"/></g></svg>www.brevlo.com.au</span>
  </div>
</div>
</body>
</html>
```